OTU Consulting Firm needs artwork for foyer

We are looking for a piece of artwork for our foyer entrance. It will be displayed on the white wall above the two armchairs.

The piece could be meaningful to our organisation, but also could be of an abstract nature. We want the artwork to be striking/interesting as it is displayed in the foyer. The artwork would be printed on a landscape canvas print with dimensions 76 cm x 152 cm.

Please see attached word document "Velm Studio" for all specifications.

Target Market(s)

Industry/Entity Type

Consulting

Requirements
Must have
• Please see attached word document "Velm Studio" for all specifications.
Nice to have
Should not have

```html
<!DOCTYPE html>
<html lang="en">
<head>
<meta charset="utf-8">
<title>OTU Consulting Firm — Foyer Artwork</title>
<link rel="stylesheet" href="https://fonts.googleapis.com/css2?family=Montserrat:wght@200;300;400;800&family=Yesteryear&family=Patrick+Hand&family=Advent+Pro:wght@400&family=Tinos&family=Abril+Fatface&display=swap">
<style>
  :root {
    --sky: #6ab2e4;
    --stripe: #c2c3c6;
    --map: #2f7cc0;
    --ink: #111111;
    --grey: #7d7d7d;
    --white: #f4f6f8;
    --royal: #1f6fb5;
    --teal: #2aa0a8;
    --navy: #17529a;
    --page: #ffffff;
  }
  html, body {
    margin: 0;
    width: 1200px;
    height: 674px;
    overflow: hidden;
    background: var(--page);
  }
  .stage {
    position: relative;
    width: 1200px;
    height: 674px;
  }
  .artwork {
    position: absolute;
    left: 48px;
    top: 58px;
    width: 1112px;
    height: 556px;
    background: var(--sky);
    overflow: hidden;
  }
  .world-map {
    position: absolute;
    left: 140px;
    top: 40px;
    width: 860px;
    height: 470px;
    border-radius: 45%;
    background: radial-gradient(ellipse at center, rgba(47,124,192,0.85) 0%, rgba(47,124,192,0.55) 55%, rgba(47,124,192,0) 75%);
  }
  .bubble-trail {
    position: absolute;
    left: 70px;
    top: 50px;
    width: 190px;
    height: 480px;
    border-radius: 50%;
    background: radial-gradient(ellipse at center, rgba(220,236,240,0.55) 0%, rgba(220,236,240,0) 70%);
  }
  .globe {
    position: absolute;
    left: 740px;
    top: 62px;
    width: 264px;
    height: 264px;
    border-radius: 50%;
    background: radial-gradient(circle at 40% 38%, #cfe3f3 0%, #8fbde3 45%, #3d84c4 100%);
    opacity: 0.9;
  }
  .cloud {
    position: absolute;
    left: 412px;
    top: 454px;
    width: 208px;
    height: 88px;
    border-radius: 44px;
    background: linear-gradient(180deg, #f2f8fc 0%, #d2e6f4 100%);
  }
  .stripes {
    position: absolute;
    inset: 0;
    background: repeating-linear-gradient(180deg, var(--stripe) 0 5px, transparent 5px 21.6px);
    background-position: 0 10px;
  }
  .word {
    position: absolute;
    margin: 0;
    white-space: nowrap;
    line-height: 1;
  }
  .supportive-vertical {
    left: 12px; top: 258px;
    font: 300 38px "Montserrat", sans-serif;
    color: var(--ink);
    transform: rotate(-90deg);
    transform-origin: left top;
  }
  .growth {
    left: 330px; top: 20px;
    font: 400 96px "Yesteryear", cursive;
    color: var(--white);
  }
  .quality-script {
    left: 84px; top: 112px;
    font: 400 36px "Abril Fatface", serif;
    font-style: italic;
    color: var(--ink);
  }
  .client-focus {
    left: 222px; top: 158px;
    font: 200 58px "Montserrat", sans-serif;
    color: var(--grey);
  }
  .supportive-small {
    left: 396px; top: 228px;
    font: italic 400 18px "Abril Fatface", serif;
    color: var(--ink);
  }
  .excellence {
    left: 122px; top: 246px;
    font: italic 400 50px "Abril Fatface", serif;
    color: var(--royal);
  }
  .collaboration {
    left: 372px; top: 318px;
    font: 400 50px "Tinos", serif;
    color: var(--grey);
  }
  .development {
    left: 310px; top: 392px;
    font: italic 400 24px "Abril Fatface", serif;
    color: var(--ink);
  }
  .accountability-teal {
    left: 560px; top: 388px;
    font: 400 70px "Advent Pro", sans-serif;
    color: var(--teal);
    transform: scaleX(0.78);
    transform-origin: left top;
  }
  .positive {
    left: 26px; top: 426px;
    font: 400 86px "Patrick Hand", cursive;
    color: var(--ink);
  }
  .accountability-hand {
    left: 804px; top: 6px;
    font: 400 52px "Patrick Hand", cursive;
    color: var(--ink);
  }
  .quality-vertical {
    left: 1096px; top: 60px;
    font: 200 44px "Montserrat", sans-serif;
    color: var(--grey);
    transform: rotate(90deg);
    transform-origin: left top;
  }
  .integrity {
    left: 1108px; top: 174px;
    font: 800 46px "Montserrat", sans-serif;
    color: var(--ink);
    transform: rotate(90deg);
    transform-origin: left top;
  }
  .client-focus-small {
    left: 854px; top: 490px;
    font: italic 400 19px "Abril Fatface", serif;
    color: var(--grey);
  }
  .firm-name {
    position: absolute;
    left: 984px; top: 496px;
    display: flex;
    align-items: center;
    gap: 8px;
  }
  .firm-name .mark {
    width: 14px; height: 14px;
    background: var(--navy);
  }
  .firm-name .label {
    font: 800 44px "Montserrat", sans-serif;
    color: var(--navy);
    line-height: 1;
  }
</style>
</head>
<body>
<main class="stage">
  <section class="artwork" aria-label="OTU Consulting Firm foyer artwork">
    <div class="world-map" role="img" aria-label="World map silhouette in deep blue"></div>
    <div class="bubble-trail" role="img" aria-label="Trail of pale floating bubbles"></div>
    <div class="globe" role="img" aria-label="Lattice globe with orbit rings"></div>
    <div class="cloud" role="img" aria-label="Soft white cloud"></div>
    <div class="stripes"></div>

    <p class="word supportive-vertical">Supportive</p>
    <p class="word growth">Growth</p>
    <p class="word quality-script">Quality</p>
    <p class="word client-focus">Client Focus</p>
    <p class="word supportive-small">Supportive</p>
    <p class="word excellence">Excellence</p>
    <p class="word collaboration">COLLABORATION</p>
    <p class="word development">Development</p>
    <p class="word accountability-teal">Accountability</p>
    <p class="word positive">Positive</p>
    <p class="word accountability-hand">Accountability</p>
    <p class="word quality-vertical">Quality</p>
    <p class="word integrity">INTEGRITY</p>
    <p class="word client-focus-small">Client Focus</p>

    <div class="firm-name">
      <span class="mark"></span>
      <span class="label">OTU</span>
    </div>
  </section>
</main>
</body>
</html>
```